Leaflet design to advertise new event management system

We are a software company based in Greater London and are in need of a leaflet design to advertise 'Velmaro'- a new event competition management system.
The leaflet will be distributed around event competitions (such as flower shows or kids competitions) to market the product and pick up prospective clients.
Velmaro is easy and simple, and we would like the design to reflect that.
We would like to see designs which use our orange #f05f40
Please see attached for a rough example of what we are hoping for and visit www.velmaro-example.com for more inspiration.

Industry/Entity Type

It Company

```html
<!DOCTYPE html>
<html lang="en">
<head>
<meta charset="utf-8">
<title>Velmaro Livestream Leaflet</title>
<link href="https://fonts.googleapis.com/css2?family=Open+Sans:wght@400;600;700&family=Roboto+Condensed:wght@700&display=swap" rel="stylesheet">
<style>
  :root {
    --orange: #f05f40;
    --ink: #3a3a3a;
    --text: #333333;
    --white: #ffffff;
    --photo-pink: #e0406a;
    --photo-red: #c8283c;
    --photo-violet: #8a3a7a;
    --photo-green: #4f7a3a;
    --device: #141414;
    --screen: #f4f4f4;
  }
  * { box-sizing: border-box; margin: 0; padding: 0; }
  html, body { width: 899px; height: 1200px; overflow: hidden; background: var(--white); }
  body { font-family: "Open Sans", Arial, sans-serif; color: var(--text); }
  .leaflet { position: relative; width: 899px; height: 1200px; overflow: hidden; background: var(--white); }

  .hero { position: absolute; left: 0; top: 0; width: 899px; height: 500px; }
  .hero svg { display: block; }
  .brand-name { position: absolute; left: 38px; top: 232px; font-size: 36px; font-weight: 700; color: var(--orange); letter-spacing: 1px; }
  .hero-points { position: absolute; left: 40px; top: 350px; list-style: none; color: var(--white); font-size: 19px; font-weight: 600; line-height: 30px; }
  .hero-points li { padding-left: 18px; position: relative; }
  .hero-points li::before { content: "•"; position: absolute; left: 0; }

  .app-preview { position: absolute; left: 570px; top: 105px; width: 226px; height: 400px; border-radius: 26px; background: var(--device); padding: 28px 14px 58px; }
  .app-preview .screen { width: 100%; height: 100%; background: var(--screen); border-radius: 3px; }
  .app-preview .home-key { position: absolute; left: 50%; bottom: 14px; width: 32px; height: 32px; margin-left: -16px; border-radius: 50%; background: var(--white); }

  .headline { position: absolute; left: 0; top: 528px; width: 899px; text-align: center; font-family: "Roboto Condensed", "Arial Narrow", sans-serif; font-weight: 700; font-size: 44px; color: var(--ink); letter-spacing: 0.5px; }
  .headline span { color: var(--orange); }

  .section-title { position: absolute; left: 60px; width: 779px; display: flex; align-items: center; gap: 22px; color: var(--orange); font-weight: 600; font-size: 27px; letter-spacing: 1px; white-space: nowrap; }
  .section-title::before, .section-title::after { content: ""; flex: 1; height: 8px; border-top: 2px solid var(--orange); border-bottom: 2px solid var(--orange); }
  .talk-title { top: 596px; }
  .do-title { top: 985px; }

  .lead { position: absolute; left: 70px; width: 759px; text-align: center; font-size: 17px; font-weight: 700; line-height: 26px; color: var(--text); }
  .talk-lead { top: 642px; }
  .do-lead { top: 1030px; font-weight: 600; }

  .features { position: absolute; left: 0; top: 710px; width: 899px; height: 262px; background: var(--orange); display: flex; justify-content: space-around; padding: 30px 40px 0; }
  .feature { width: 180px; text-align: center; color: var(--white); }
  .feature-icon { width: 66px; height: 66px; margin: 0 auto 16px; border-radius: 50%; background: var(--white); display: flex; align-items: center; justify-content: center; }
  .feature h3 { font-size: 16px; font-weight: 600; margin-bottom: 6px; }
  .feature p { font-size: 13.5px; font-weight: 600; line-height: 19px; }

  .contacts { position: absolute; left: 0; top: 1100px; width: 899px; height: 26px; font-style: normal; font-size: 16.5px; font-weight: 600; color: var(--text); }
  .contact { position: absolute; top: 0; display: flex; align-items: center; gap: 10px; white-space: nowrap; }
  .contact-phone { left: 62px; }
  .contact-mail { left: 318px; }
  .contact-web { left: 606px; }
  .footer-band { position: absolute; left: 0; bottom: 0; width: 899px; height: 30px; background: var(--orange); }
</style>
</head>
<body>
<main class="leaflet">
  <header class="hero">
    <svg width="899" height="500" viewBox="0 0 899 500">
      <defs>
        <linearGradient id="flowerField" x1="0" y1="0" x2="1" y2="1">
          <stop offset="0" stop-color="#c8283c"/>
          <stop offset="0.35" stop-color="#e0406a"/>
          <stop offset="0.7" stop-color="#8a3a7a"/>
          <stop offset="1" stop-color="#4f7a3a"/>
        </linearGradient>
      </defs>
      <rect class="hero-photo" width="899" height="470" fill="url(#flowerField)" role="img" aria-label="Photograph of tall pink, red and purple lupin flowers in a garden"/>
      <path class="hero-panel" d="M0,190 C120,158 260,168 330,255 C400,345 520,400 899,418 L899,500 L0,500 Z" fill="#ffffff"/>
      <path class="hero-band" d="M0,327 L350,327 C410,327 440,375 510,412 C600,458 750,462 899,452 L899,484 C750,498 600,494 505,474 C430,460 370,457 0,457 Z" fill="#f05f40"/>
    </svg>
    <div class="brand-name">VELMARO</div>
    <ul class="hero-points">
      <li>Publish results as they happen</li>
      <li>Keep up to date with the events<br>top scorers</li>
    </ul>
    <div class="app-preview" role="img" aria-label="Phone showing the Velmaro live results screen for a flower show">
      <div class="screen"></div>
      <div class="home-key"></div>
    </div>
  </header>

  <h1 class="headline">INTRODUCING <span>VELMARO</span> LIVESTREAM</h1>

  <h2 class="section-title talk-title">LET’S TALK</h2>
  <p class="lead talk-lead">Ready to try out Velmaro to manage your event competitions? That's great! Give us a call or send us an email and we will get back to you as soon as possible!</p>

  <section class="features">
    <div class="feature">
      <div class="feature-icon">
        <svg width="34" height="30" viewBox="0 0 34 30" fill="none" stroke="#f05f40" stroke-width="2.4" stroke-linejoin="round"><path d="M8,2 H26 L32,10 L17,28 L2,10 Z M2,10 H32 M12,2 L10,10 L17,28 L24,10 L22,2"/></svg>
      </div>
      <h3>Event Templates</h3>
      <p>Build one or more competition templates for repeating events</p>
    </div>
    <div class="feature">
      <div class="feature-icon">
        <svg width="32" height="32" viewBox="0 0 32 32"><path d="M30,2 L2,14 L12,18 L14,29 L19,21 Z" fill="#f05f40"/></svg>
      </div>
      <h3>Your Competitions</h3>
      <p>Competition sections, categories and classes keep your lupins from your Victoria sponges</p>
    </div>
    <div class="feature">
      <div class="feature-icon">
        <svg width="34" height="28" viewBox="0 0 34 28" fill="none" stroke="#f05f40" stroke-width="2.4"><rect x="5" y="2" width="27" height="24" rx="2"/><path d="M5,8 H2 V24 a2,2 0 0 0 3,2"/><rect x="10" y="7" width="9" height="7" fill="#f05f40" stroke="none"/><path d="M22,8 H28 M22,13 H28 M10,18 H28 M10,22 H28"/></svg>
      </div>
      <h3>Online entry</h3>
      <p>Invite your competitors to sign up online.</p>
    </div>
    <div class="feature">
      <div class="feature-icon">
        <svg width="34" height="30" viewBox="0 0 34 30"><path d="M17,29 L4,16 A8,8 0 0 1 17,5 A8,8 0 0 1 30,16 Z" fill="#f05f40"/></svg>
      </div>
      <h3>Instant results</h3>
      <p>Publish your competition results straight to the web!</p>
    </div>
  </section>

  <h2 class="section-title do-title">WHAT DO WE DO?</h2>
  <p class="lead do-lead">Velmaro has everything you need to get your event competition up and running in no time!</p>

  <address class="contacts">
    <div class="contact contact-phone">
      <svg width="20" height="20" viewBox="0 0 20 20"><rect width="20" height="20" rx="3" fill="#f05f40"/><path d="M6,4 L8.5,4 L9.5,7.5 L8,8.7 C8.8,10.5 9.8,11.5 11.4,12.2 L12.6,10.7 L16,11.7 L16,14.2 C10,15 5,10 6,4 Z" fill="#ffffff"/></svg>
      <span>0845 000 4821</span>
    </div>
    <div class="contact contact-mail">
      <svg width="22" height="16" viewBox="0 0 22 16" fill="none" stroke="#f05f40" stroke-width="1.8"><rect x="1" y="1" width="20" height="14"/><path d="M1,1 L11,9 L21,1"/></svg>
      <span>hello@velmaro-example.com</span>
    </div>
    <div class="contact contact-web">
      <svg width="18" height="18" viewBox="0 0 18 18" fill="none" stroke="#f05f40" stroke-width="1.5"><circle cx="9" cy="9" r="7.5"/><ellipse cx="9" cy="9" rx="3.2" ry="7.5"/><path d="M1.5,9 H16.5 M3,5 H15 M3,13 H15"/></svg>
      <span>www.velmaro-example.com</span>
    </div>
  </address>

  <div class="footer-band"></div>
</main>
</body>
</html>
```